Linkmesa and Glimtoria advertising

We need Linkmesa and Glimtoria ads. Simple ad with Alaska themed background.
This ad is to introduce our new ZENIRO Internet service.
--Speeds to 500 mpbs
-- Packages start at only $89.99 for speeds to 100mbps
-- Fiber Optic based connection, Not satellite
-- Extreme low latency, consistent speeds
--FREE equipment, FREE Installation, FREE wifi router, First month of service FREE

```html
<!DOCTYPE html>
<html lang="en">
<head>
<meta charset="UTF-8">
<title>ZENIRO Internet – Launch Ad</title>
<link rel="stylesheet" href="https://fonts.googleapis.com/css2?family=Bebas+Neue&family=Antonio:wght@400&family=Barlow+Condensed:wght@600&family=Montserrat:wght@400&display=swap">
<style>
  :root {
    --stage: #8c8c8c;
    --paper: #ffffff;
    --brand-blue: #0b4c9c;
    --deep-blue: #0a4496;
    --brand-red: #e8000d;
    --band-red: #ee1b24;
    --navy: #0c1f3a;
    --ink: #111827;
    --white: #ffffff;
  }
  * { margin: 0; padding: 0; box-sizing: border-box; }
  html, body { width: 1200px; height: 978px; overflow: hidden; background: var(--stage); }
  .ad {
    position: absolute; left: 111px; top: 0;
    width: 978px; height: 978px;
    background: var(--paper); overflow: hidden;
  }
  .abs { position: absolute; }

  .brand-tile {
    left: 61px; top: 57px; width: 207px; height: 108px;
    background: var(--navy);
    display: flex; align-items: flex-end; padding: 0 0 18px 18px;
    font-family: "Bebas Neue", sans-serif; font-size: 34px; color: var(--white);
    letter-spacing: 1px;
  }
  .partner-name {
    left: 309px; top: 108px;
    font-family: "Barlow Condensed", sans-serif; font-weight: 600;
    font-size: 53px; line-height: 1; color: var(--ink); white-space: nowrap;
  }
  .headline {
    left: 61px; top: 190px;
    font-family: "Bebas Neue", sans-serif; font-weight: 400; font-size: 86px; line-height: 1;
    color: var(--brand-blue); white-space: nowrap;
  }
  .scene-photo {
    left: 0; top: 350px; width: 978px; height: 460px;
    background: linear-gradient(180deg, #5d6f86 0%, #8b9aad 28%, #d9dfe6 48%, #7f8b96 62%, #c9d2da 72%, #3f5466 78%, #2e4456 100%);
  }
  .band-shape, .sea-shape { left: 0; }
  .band-text {
    left: 65px; top: 288px;
    font-family: "Antonio", sans-serif; font-size: 50px; line-height: 1;
    color: var(--white); white-space: nowrap; text-transform: uppercase;
  }

  .offer {
    width: 206px; height: 206px; border-radius: 50%;
    display: flex; flex-direction: column; align-items: center; justify-content: center;
    color: var(--white); text-align: center; text-transform: uppercase;
  }
  .offer.red { background: var(--brand-red); }
  .offer.blue { background: var(--deep-blue); }
  .offer.ringed { box-shadow: 0 0 0 18px rgba(255,255,255,0.35); }
  .offer-free { font-family: "Bebas Neue", sans-serif; font-size: 64px; line-height: 0.9; }
  .offer-item { font-family: "Antonio", sans-serif; font-size: 34px; line-height: 1.05; white-space: nowrap; }

  .price-text {
    font-family: "Bebas Neue", sans-serif; color: var(--white); white-space: nowrap; line-height: 1;
  }
  .price-label { top: 858px; font-size: 36px; }
  .price-big { top: 842px; font-size: 66px; }
  .underline-arrow { top: 889px; }
  .feature {
    top: 911px; display: flex; align-items: center; gap: 10px;
    font-family: "Montserrat", sans-serif; font-size: 19px; color: var(--white); white-space: nowrap;
  }
</style>
</head>
<body>
<main class="ad">
  <div class="abs brand-tile">ZENIRO</div>
  <div class="abs partner-name">Crestline Satellite</div>
  <h1 class="abs headline">SPEEDS TO 500 MPBS</h1>

  <div class="abs scene-photo" role="img" aria-label="Snow-covered Alaskan mountains under a cloudy sky above a choppy sea"></div>

  <svg class="abs band-shape" style="top:272px" width="978" height="90" viewBox="0 0 978 90" aria-hidden="true">
    <polygon fill="var(--band-red)" points="0,2 700,0 712,10 700,18 718,26 696,36 712,46 690,56 704,66 684,76 696,84 670,88 0,88"/>
  </svg>
  <div class="abs band-text">First month of service free</div>

  <svg class="abs sea-shape" style="top:770px" width="978" height="208" viewBox="0 0 978 208" aria-hidden="true">
    <polygon fill="var(--brand-blue)" points="0,50 60,44 140,36 230,30 300,18 380,22 460,14 540,20 620,10 700,6 780,0 860,-10 930,-20 978,-30 978,208 0,208"/>
  </svg>

  <div class="abs offer red" style="left:705px; top:42px">
    <span class="offer-free">Free</span><span class="offer-item">Equipment</span>
  </div>
  <div class="abs offer blue ringed" style="left:705px; top:288px">
    <span class="offer-free">Free</span><span class="offer-item">Installation</span>
  </div>
  <div class="abs offer red ringed" style="left:705px; top:542px">
    <span class="offer-free">Free</span><span class="offer-item">WiFi Router</span>
  </div>

  <div class="abs price-text price-label" style="left:62px">Packages start at only</div>
  <div class="abs price-text price-big" style="left:356px">$89.99</div>
  <div class="abs price-text price-label" style="left:532px">For speeds to</div>
  <div class="abs price-text price-big" style="left:717px">100MBPS</div>

  <svg class="abs underline-arrow" style="left:62px" width="274" height="10" viewBox="0 0 274 10" aria-hidden="true">
    <line x1="0" y1="5" x2="266" y2="5" stroke="var(--brand-red)" stroke-width="2"/>
    <polygon points="264,0 274,5 264,10" fill="var(--brand-red)"/>
  </svg>
  <svg class="abs underline-arrow" style="left:532px" width="166" height="10" viewBox="0 0 166 10" aria-hidden="true">
    <line x1="0" y1="5" x2="158" y2="5" stroke="var(--brand-red)" stroke-width="2"/>
    <polygon points="156,0 166,5 156,10" fill="var(--brand-red)"/>
  </svg>

  <div class="abs feature" style="left:62px">
    <svg width="26" height="26" viewBox="0 0 26 26" aria-hidden="true"><circle cx="13" cy="13" r="13" fill="var(--brand-red)"/><polyline points="7,13 11.5,17.5 19,9" fill="none" stroke="var(--white)" stroke-width="3"/></svg>
    Fiber Optic based connection, Not satellite
  </div>
  <div class="abs feature" style="left:525px">
    <svg width="26" height="26" viewBox="0 0 26 26" aria-hidden="true"><circle cx="13" cy="13" r="13" fill="var(--brand-red)"/><polyline points="7,13 11.5,17.5 19,9" fill="none" stroke="var(--white)" stroke-width="3"/></svg>
    Extreme low latency, consistent speeds
  </div>
</main>
</body>
</html>
```